Amazing Sexy Elegant Eyecatching Wine Label

We need a label designed for our wine which is going to be produced very soon.

Needs to be on a grey scale, as colours increase the price per label dramatically.

Needs to have the "Crown" logo (file attached) included on the front and back label. Logo can be in black/white but can not be changed in any way, circle around the crown must stay there as well.

We are still unsure of whether to use "Harrowby Wine" or "Harrowby" as the brand for the label, if you could submit designs based around the two names we would appreciate that.

We will have 5 varieties, including; Sauvignon Blanc, Chardonnay, Pinot Gris, Riesling and Pinot Noir. So text needs to be easily changed.

We are after an image on the label which is modern and eye catching, even in a grey scale.

Please see other attached files for an idea we have done previously, we want something a bit more "designer" though. Some information on the label is a legal requirement and needs to be kept.

Target Market(s)

Wine Consumers

Requirements
Must have
• Crown Logo, Harrowby/Harrowby Wine brand, Grey Scale, Modern Design

```html
<!DOCTYPE html>
<html lang="en">
<head>
<meta charset="utf-8">
<title>Harrowby Wine – Label Set</title>
<link rel="stylesheet" href="https://fonts.googleapis.com/css2?family=Tinos:wght@400;700&display=swap">
<style>
  :root {
    --page: #ffffff;
    --label: #232323;
    --label-stripe: #262626;
    --ink: #ffffff;
    --range-light: #4a4a4a;
    --range-dark: #2b2b2b;
  }
  * { margin: 0; padding: 0; box-sizing: border-box; }
  html, body {
    width: 1200px; height: 960px; overflow: hidden;
    background: var(--page);
  }
  .canvas { position: relative; width: 1200px; height: 960px; }
  .label {
    position: absolute; top: 91px; width: 483px; height: 744px;
    background: linear-gradient(160deg, var(--label-stripe) 0%, var(--label) 45%, var(--label) 100%);
    color: var(--ink);
    font-family: "Tinos", "Times New Roman", serif;
    text-align: center;
    overflow: hidden;
  }
  .label--back { left: 72px; }
  .label--front { left: 611px; }

  .brand-mark { position: absolute; left: 50%; transform: translateX(-50%); }
  .brand-mark text { font-family: "Tinos", "Times New Roman", serif; fill: var(--ink); }

  .range-band {
    position: absolute; left: 0; width: 100%; height: 120px; top: 445px;
    background: linear-gradient(180deg, var(--range-light) 0%, var(--range-dark) 70%, var(--label) 100%);
    opacity: .85;
  }

  .brand-name { position: absolute; left: 0; width: 100%; font-weight: 400; line-height: 1; }
  .label--back .brand-name { top: 184px; font-size: 38px; }
  .label--front .brand-name { top: 288px; font-size: 47px; }

  .tasting-notes {
    position: absolute; top: 242px; left: 30px; right: 30px;
    font-size: 16px; line-height: 27px;
  }
  .tasting-notes p + p { margin-top: 6px; }
  .web {
    position: absolute; top: 473px; left: 0; width: 100%;
    font-size: 22px; line-height: 26px;
  }

  .legal {
    position: absolute; left: 40px; top: 602px; text-align: left;
    text-transform: uppercase;
  }
  .legal .heading { font-size: 15px; line-height: 18px; }
  .legal .detail { font-size: 8.5px; line-height: 11px; margin-bottom: 10px; }
  .legal .notice { font-size: 15px; line-height: 18px; margin-top: 3px; }

  .variety-block { position: absolute; left: 0; width: 100%; top: 566px; }
  .region { font-size: 22px; letter-spacing: .5px; }
  .variety { font-size: 32px; letter-spacing: 1.5px; margin-top: 14px; }
  .vintage { font-size: 22px; margin-top: 6px; }
  .origin { font-size: 12px; margin-top: 28px; letter-spacing: .5px; }
</style>
</head>
<body>
<main class="canvas">

  <section class="label label--back" aria-label="Back label">
    <svg class="brand-mark" style="top:53px" width="120" height="120" viewBox="0 0 120 120">
      <circle cx="60" cy="60" r="57" fill="none" stroke="#ffffff" stroke-width="3"/>
      <text x="60" y="66" font-size="17" text-anchor="middle">Harrowby</text>
    </svg>
    <h1 class="brand-name">Harrowby Wine</h1>
    <div class="tasting-notes">
      <p>Crisp, light amber color with good acid.<br>The nose is reminiscent of freshly cut<br>herbs with a hint of mint.</p>
      <p>It will enhance rather than overpower<br>any dish. A wonderful complement to<br>any light dish and delightfully refreshing.<br>Serve lightly chilled.</p>
    </div>
    <div class="range-band" role="img" aria-label="Grey mountain range silhouette across the label"></div>
    <p class="web">www.harrowbyimports.co.nz</p>
    <div class="legal">
      <p class="heading">Produced and bottled by</p>
      <p class="detail">Kestrel Ridge Wines Marlborough, NZ</p>
      <p class="heading">Distributed by</p>
      <p class="detail">Harrowby Imports Ltd.</p>
      <p class="notice">Drink responsibily</p>
    </div>
  </section>

  <section class="label label--front" aria-label="Front label">
    <svg class="brand-mark" style="top:94px" width="154" height="154" viewBox="0 0 154 154">
      <circle cx="77" cy="77" r="74" fill="none" stroke="#ffffff" stroke-width="3.5"/>
      <text x="77" y="84" font-size="22" text-anchor="middle">Harrowby</text>
    </svg>
    <h1 class="brand-name">Harrowby Wine</h1>
    <div class="range-band" role="img" aria-label="Grey mountain range silhouette across the label"></div>
    <div class="variety-block">
      <p class="region">MARLBOUGH</p>
      <p class="variety">SAUVIGNON BLANC</p>
      <p class="vintage">2015</p>
      <p class="origin">WINE OF NEW ZEALAND</p>
    </div>
  </section>

</main>
</body>
</html>
```